Luminously Grounded Vitality

We want to design a business card that is modern and appealing for an innovative psychedelic telemedicine company that provides at-home ketamine-assisted therapy along with wellness, longevity, and anti-aging medicines. We want to use our deep purple and white plus other colors you can find on our website. We don't have any strict brand guidelines yet so feel free to get creative. We want a very professional, but technology first modern design that will instill trust, peace, calm, but also be attractive to investors in the healthcare and SaaS space.

```html
<!DOCTYPE html>
<html lang="en">
<head>
<meta charset="utf-8">
<title>Luminously Grounded Vitality – Business Card</title>
<link rel="stylesheet" href="https://fonts.googleapis.com/css2?family=Alegreya+Sans:wght@400&family=Montserrat:wght@700&family=Open+Sans:wght@600&display=swap">
<style>
  :root {
    --stage: #e3e6ec;
    --card-white: #f3f1fd;
    --card-lilac: #e6def6;
    --plum: #5c2c4b;
    --navy-violet: #2c2650;
    --orchid: #b67ab6;
    --orchid-deep: #a963a6;
    --lavender: #857bbd;
    --ink: #2b2b33;
    --ink-soft: #3a3a44;
    --bar-start: #b27fbe;
    --bar-end: #6a4c8f;
  }
  html, body {
    margin: 0;
    width: 1200px;
    height: 1200px;
    overflow: hidden;
    background: var(--stage);
  }
  .stage {
    position: relative;
    width: 1200px;
    height: 1200px;
  }
  .card {
    position: absolute;
    left: 303px;
    width: 594px;
    height: 346px;
    box-shadow: 0 2px 6px rgba(60, 60, 90, 0.12);
  }
  .card--front { top: 229px; }
  .card--back { top: 624px; }
  .card svg { display: block; width: 100%; height: 100%; }
  .brand-name {
    font-family: "Alegreya Sans", sans-serif;
    font-weight: 400;
    fill: var(--orchid);
  }
  .holder-name {
    font-family: "Montserrat", sans-serif;
    font-weight: 700;
    fill: var(--ink);
    letter-spacing: 1px;
  }
  .contact-line {
    font-family: "Open Sans", sans-serif;
    font-weight: 600;
    fill: var(--ink-soft);
    letter-spacing: 1px;
  }
  .web-address {
    font-family: "Open Sans", sans-serif;
    font-weight: 600;
    fill: #ffffff;
    letter-spacing: 3px;
  }
</style>
</head>
<body>
<main class="stage">

  <section class="card card--front" aria-label="Business card front">
    <svg viewBox="0 0 956 556" xmlns="http://www.w3.org/2000/svg">
      <defs>
        <linearGradient id="front-surface" x1="0" y1="0" x2="1" y2="1">
          <stop offset="0" stop-color="#d4d7e8"/>
          <stop offset="0.45" stop-color="var(--card-white)"/>
          <stop offset="1" stop-color="var(--card-lilac)"/>
        </linearGradient>
        <radialGradient id="front-glow-top" cx="0" cy="0" r="1">
          <stop offset="0" stop-color="var(--plum)"/>
          <stop offset="0.55" stop-color="var(--navy-violet)" stop-opacity="0.6"/>
          <stop offset="1" stop-color="var(--navy-violet)" stop-opacity="0"/>
        </radialGradient>
        <radialGradient id="front-glow-bottom" cx="1" cy="1" r="1">
          <stop offset="0" stop-color="var(--orchid)"/>
          <stop offset="0.55" stop-color="var(--lavender)" stop-opacity="0.55"/>
          <stop offset="1" stop-color="var(--lavender)" stop-opacity="0"/>
        </radialGradient>
      </defs>
      <rect class="surface" width="956" height="556" fill="url(#front-surface)"/>
      <rect class="accent-area accent-area--top" width="400" height="340" fill="url(#front-glow-top)"
            role="img" aria-label="Decorative plum and navy flowing accent"/>
      <rect class="accent-area accent-area--bottom" x="656" y="256" width="300" height="300" fill="url(#front-glow-bottom)"
            role="img" aria-label="Decorative orchid and lavender flowing accent"/>

      <circle class="brand-mark" cx="238" cy="282" r="18" fill="var(--navy-violet)"/>
      <text class="brand-name" x="272" y="300" font-size="50">Luminously Grounded Vitality</text>
    </svg>
  </section>

  <section class="card card--back" aria-label="Business card back">
    <svg viewBox="0 0 956 556" xmlns="http://www.w3.org/2000/svg">
      <defs>
        <linearGradient id="back-surface" x1="0" y1="0" x2="1" y2="1">
          <stop offset="0" stop-color="var(--card-white)"/>
          <stop offset="0.6" stop-color="#ece8fb"/>
          <stop offset="1" stop-color="#d6cce6"/>
        </linearGradient>
        <linearGradient id="back-side" x1="0" y1="0" x2="1" y2="0">
          <stop offset="0" stop-color="var(--orchid-deep)"/>
          <stop offset="0.55" stop-color="var(--orchid)" stop-opacity="0.9"/>
          <stop offset="0.8" stop-color="var(--lavender)" stop-opacity="0.5"/>
          <stop offset="1" stop-color="var(--lavender)" stop-opacity="0"/>
        </linearGradient>
        <linearGradient id="web-bar" x1="0" y1="0" x2="1" y2="0">
          <stop offset="0" stop-color="var(--bar-start)"/>
          <stop offset="1" stop-color="var(--bar-end)"/>
        </linearGradient>
      </defs>
      <rect class="surface" width="956" height="556" fill="url(#back-surface)"/>
      <rect class="accent-area accent-area--side" width="360" height="556" fill="url(#back-side)"
            role="img" aria-label="Decorative orchid and lavender flowing side panel"/>

      <text class="holder-name" x="880" y="165" font-size="34" text-anchor="end">YOUR NAME</text>

      <g class="contact">
        <text class="contact-line" x="828" y="264" font-size="20" text-anchor="end">+(01) 1234 5678 901</text>
        <circle cx="864" cy="258" r="15" fill="var(--orchid-deep)"/>
        <path d="M857 251 c2-2 4-1 5 1 l1 3 c0 1-1 2-2 2 c1 3 3 5 6 6 c0-1 1-2 2-2 l3 1 c2 1 3 3 1 5 c-8 2-17-7-16-16 z" fill="#ffffff"/>

        <text class="contact-line" x="828" y="316" font-size="20" text-anchor="end">yourmail@email.com</text>
        <circle cx="864" cy="310" r="15" fill="var(--orchid-deep)"/>
        <rect x="855" y="304" width="18" height="12" rx="1.5" fill="#ffffff"/>
        <path d="M855 305 L864 312 L873 305" fill="none" stroke="var(--orchid-deep)" stroke-width="1.6"/>

        <text class="contact-line" x="828" y="366" font-size="20" text-anchor="end">Your Street Address Here</text>
        <text class="contact-line" x="828" y="388" font-size="20" text-anchor="end">Location Lorem Ipsum</text>
        <circle cx="864" cy="371" r="15" fill="var(--orchid-deep)"/>
        <path d="M864 382 C858 375 856 371 856 367 a8 8 0 0 1 16 0 c0 4-2 8-8 15 z" fill="#ffffff"/>
        <circle cx="864" cy="367" r="3" fill="var(--orchid-deep)"/>
      </g>

      <path class="web-bar" d="M386 443 L956 443 L956 498 L386 498 a27.5 27.5 0 0 1 0-55 z" fill="url(#web-bar)"/>
      <text class="web-address" x="644" y="478" font-size="20" text-anchor="middle">WWW.YOURWEBSITE.COM</text>
    </svg>
  </section>

</main>
</body>
</html>
```